Bicycle Sales Company

I need a bicycle sales site for pre-orders, 3-4 models, multiple colors per order. The bikes are electric bikes, company logo color scheme has red. Maybe a countdown to a date when pre-order will close. I also want to incorporate a deposit style system for the pre-order with the balance due on shipping.

Coding

Coded - Design and coding required

```html
<!DOCTYPE html>
<html lang="en">
<head>
<meta charset="utf-8">
<title>VoltRide — Electric Bikes Pre-Order</title>
<link href="https://fonts.googleapis.com/css2?family=Playfair+Display:wght@400;700&family=Lato:wght@400;700&display=swap" rel="stylesheet">
<style>
:root{
  --red:#e8141b;
  --ink:#1e1e22;
  --text:#3c3c42;
  --muted:#6c6c72;
  --hero-bg:#f2f2f2;
  --section-bg:#ececec;
  --light-bg:#f1f1f1;
  --white:#ffffff;
  --dark:#25252f;
  --dark-box:#2b2b2e;
  --price:#b7632c;
  --swatch-red:#e8141b;
  --swatch-graphite:#3a3d42;
  --swatch-white:#f4f4f4;
  --swatch-teal:#2f8f8a;
  --swatch-sand:#c9b48a;
}
*{margin:0;padding:0;box-sizing:border-box}
html,body{width:1200px;height:4693px;overflow:hidden}
body{position:relative;background:var(--light-bg);font-family:"Lato",sans-serif;color:var(--text)}
.abs{position:absolute}
.serif{font-family:"Playfair Display",serif}
.heading{font-family:"Playfair Display",serif;font-weight:700;color:var(--ink);letter-spacing:1.5px;line-height:1.2}
.eyebrow{font-size:9px;font-weight:700;letter-spacing:.5px;text-transform:uppercase;color:var(--ink)}
.rule{width:34px;height:2px;background:var(--red)}
.copy{font-size:11px;line-height:1.6;color:var(--text)}
.btn{display:flex;align-items:center;justify-content:center;background:var(--red);color:var(--white);font-size:9px;font-weight:700;letter-spacing:.4px;text-transform:uppercase}
.photo{position:absolute}

/* hero */
.hero{left:0;top:0;width:1200px;height:657px;background:var(--white)}
.hero-panel{left:0;top:0;width:1013px;height:657px;background:var(--hero-bg)}
.nav{top:32px;font-size:12px;color:var(--ink);letter-spacing:.5px}
.brand{font-size:55px;font-weight:400;color:var(--ink);letter-spacing:1px;line-height:1}
.slider-count{top:614px;left:1047px;width:118px;display:flex;justify-content:space-between;align-items:center;font-size:8px;color:var(--ink)}

/* countdown */
.countdown{left:140px;top:546px;display:flex;align-items:center;gap:8px}
.countdown-label{font-size:9px;font-weight:700;letter-spacing:.5px;text-transform:uppercase;color:var(--ink);margin-right:8px;line-height:1.4}
.countdown-unit{width:54px;height:52px;background:var(--white);display:flex;flex-direction:column;align-items:center;justify-content:center}
.countdown-unit b{font-family:"Playfair Display",serif;font-size:20px;color:var(--ink);line-height:1}
.countdown-unit span{font-size:8px;letter-spacing:.4px;color:var(--muted);text-transform:uppercase;margin-top:4px}

/* collection */
.card{background:var(--white);width:318px;height:293px}
.card .pic{height:190px}
.card .name{text-align:center;margin-top:16px;font-family:"Playfair Display",serif;font-size:21px;color:var(--ink);line-height:1.1}
.card .price{text-align:center;margin-top:6px;font-size:13px;color:var(--price)}
.card .price small{font-size:10px;color:var(--muted)}
.swatches{display:flex;justify-content:center;gap:8px;margin-top:9px}
.swatch{width:14px;height:14px;border-radius:50%;border:1px solid #cfcfcf}
.swatch.is-selected{outline:1.5px solid var(--ink);outline-offset:2px}
.deposit-note{left:0;top:668px;width:1200px;text-align:center;font-size:10px;color:var(--muted)}

/* features */
.feature{background:var(--white);width:254px;height:160px}
.feature .label{position:absolute;left:30px;top:92px;font-family:"Playfair Display",serif;font-size:17px;line-height:1.25;color:var(--ink)}
.feature .num{position:absolute;right:26px;top:42px;font-family:"Playfair Display",serif;font-size:70px;color:#dedede;line-height:1}
.feature svg{position:absolute;left:30px;top:28px}

/* form */
.field{background:var(--white);font-size:10px;color:var(--muted);padding:14px 18px}

/* footer */
.footer{left:0;top:4301px;width:1200px;height:392px;background:var(--dark)}
.foot-label{font-size:8px;letter-spacing:.5px;color:#bdbdc4;text-transform:uppercase}
.foot-value{font-size:16px;color:var(--white)}
</style>
</head>
<body>

<!-- Hero -->
<section class="abs hero">
  <div class="abs hero-panel"></div>
  <nav>
    <span class="abs nav" style="left:331px">HOME</span>
    <span class="abs nav" style="left:435px">ABOUT US</span>
    <span class="abs nav" style="left:570px">PRODUCTS</span>
    <span class="abs nav" style="left:707px">CONTACT US</span>
  </nav>
  <div class="abs brand" style="left:148px;top:112px">VoltRide</div>
  <h1 class="abs heading" style="left:140px;top:198px;font-size:58px;width:440px;line-height:1.08">Eco-Friendly Rides, Electric Vibes</h1>
  <p class="abs copy" style="left:140px;top:398px;width:340px">Lorem ipsum dolor sit amet, consectetur adipiscing elit, sed do eiusmod tempor incididunt</p>
  <div class="abs btn" style="left:140px;top:461px;width:137px;height:55px">Pre-order now</div>
  <div class="abs countdown" aria-label="Pre-orders close countdown">
    <div class="countdown-label">Pre-orders<br>close in</div>
    <div class="countdown-unit"><b>12</b><span>Days</span></div>
    <div class="countdown-unit"><b>08</b><span>Hrs</span></div>
    <div class="countdown-unit"><b>45</b><span>Min</span></div>
    <div class="countdown-unit"><b>20</b><span>Sec</span></div>
  </div>
  <div class="photo" role="img" aria-label="Commuter in a helmet riding an electric bike along a city street" style="left:586px;top:69px;width:578px;height:519px;background:linear-gradient(135deg,#5a5e62 0%,#8a8d8c 40%,#3d4244 75%,#6b6a64 100%)"></div>
  <div class="slider-count">
    <svg width="26" height="8" viewBox="0 0 26 8"><path d="M25 4H2M5 1L2 4l3 3" stroke="#1e1e22" fill="none" stroke-width="1.2"/></svg>
    <span>1 of 3</span>
    <svg width="26" height="8" viewBox="0 0 26 8"><path d="M1 4h23M21 1l3 3-3 3" stroke="#1e1e22" fill="none" stroke-width="1.2"/></svg>
  </div>
</section>

<!-- About -->
<section class="abs" style="left:0;top:657px;width:1200px;height:621px;background:var(--white)">
  <div class="photo" role="img" aria-label="Man in a suit riding a white electric bike past a building" style="left:138px;top:104px;width:366px;height:386px;background:linear-gradient(160deg,#9fb3c8 0%,#c9c4b8 45%,#4a5a3f 80%,#2f3a2c 100%)"></div>
  <div class="abs" style="left:217px;top:406px;width:364px;height:148px;background:var(--dark-box)">
    <svg class="abs" style="left:60px;top:56px" width="40" height="40" viewBox="0 0 24 24"><path d="M6.6 3.5l2.5 2.6c.5.5.5 1.2.1 1.7L7.8 9.3c1.3 2.7 3.6 5 6.3 6.3l1.5-1.4c.5-.4 1.2-.4 1.7.1l2.6 2.5c.5.5.5 1.3 0 1.8l-1.6 1.6c-.8.8-2 1-3 .6C9.2 18.6 5.4 14.8 3.2 8.7c-.4-1-.2-2.2.6-3L5.4 4c.4-.5 1.2-.5 1.2-.5z" fill="none" stroke="#fff" stroke-width="1.1"/></svg>
    <div class="abs serif" style="left:116px;top:48px;font-size:13px;color:#ddd">For Calls:</div>
    <div class="abs serif" style="left:116px;top:70px;font-size:24px;font-weight:700;color:var(--white);white-space:nowrap">0 800-555-40-19</div>
  </div>
  <div class="abs eyebrow" style="left:661px;top:110px">About us</div>
  <h2 class="abs heading" style="left:661px;top:134px;font-size:48px;width:500px">Where Style Meets Sustainability</h2>
  <div class="abs rule" style="left:661px;top:268px"></div>
  <p class="abs copy" style="left:661px;top:296px;width:330px">Lorem ipsum dolor sit amet, consectetur adipiscing elit, sed do eiusmod tempor incididunt ut labore et dolore e magna aliqua. e magna aliqua. e magna</p>
  <p class="abs copy" style="left:661px;top:372px;width:330px">Lorem ipsum dolor sit amet, consectetur adipiscing elit, sed do eiusmod tempor incididunt ut labore et dolor e magna aliqua. e magna aliqua. e magna Lorem ipsum dolor sit amet, consectetur adipiscing elit, sed do eiusmod tempor incididunt ut labore et dolor</p>
  <div class="abs btn" style="left:661px;top:490px;width:133px;height:51px">Learn more</div>
</section>

<!-- Collection -->
<section class="abs" style="left:0;top:1278px;width:1200px;height:730px;background:var(--section-bg)">
  <div class="abs eyebrow" style="left:87px;top:97px">Our e-bikes</div>
  <h2 class="abs heading" style="left:87px;top:124px;font-size:48px">Explore the Collection</h2>
  <div class="abs rule" style="left:87px;top:211px"></div>
  <svg class="abs" style="left:27px;top:391px" width="44" height="16" viewBox="0 0 44 16"><path d="M43 8H2M9 1L2 8l7 7" stroke="#1e1e22" fill="none" stroke-width="2"/></svg>
  <svg class="abs" style="left:1114px;top:391px" width="44" height="16" viewBox="0 0 44 16"><path d="M1 8h41M35 1l7 7-7 7" stroke="#1e1e22" fill="none" stroke-width="2"/></svg>
  <article class="abs card" style="left:84px;top:270px">
    <div class="pic" role="img" aria-label="Woman with a basket bike in a park" style="background:linear-gradient(180deg,#9bb57a 0%,#6d8c52 55%,#8f8a6a 100%)"></div>
    <div class="name">Bike 1</div>
    <div class="price">$140 <small>deposit</small></div>
    <div class="swatches" aria-label="Colour options">
      <span class="swatch is-selected" style="background:var(--swatch-red)"></span>
      <span class="swatch" style="background:var(--swatch-graphite)"></span>
      <span class="swatch" style="background:var(--swatch-sand)"></span>
    </div>
  </article>
  <article class="abs card" style="left:432px;top:270px">
    <div class="pic" role="img" aria-label="Man in a jacket with a teal electric bike on a garden path" style="background:linear-gradient(180deg,#7fa05e 0%,#5d7d47 50%,#a7a9a1 100%)"></div>
    <div class="name">Bike 2</div>
    <div class="price">$140 <small>deposit</small></div>
    <div class="swatches" aria-label="Colour options">
      <span class="swatch is-selected" style="background:var(--swatch-teal)"></span>
      <span class="swatch" style="background:var(--swatch-graphite)"></span>
      <span class="swatch" style="background:var(--swatch-white)"></span>
    </div>
  </article>
  <article class="abs card" style="left:779px;top:270px">
    <div class="pic" role="img" aria-label="Rider in a suit on a white electric bike by a building" style="background:linear-gradient(180deg,#8fa9c6 0%,#b8b3a8 50%,#4b5c3e 100%)"></div>
    <div class="name">Bike 3</div>
    <div class="price">$140 <small>deposit</small></div>
    <div class="swatches" aria-label="Colour options">
      <span class="swatch is-selected" style="background:var(--swatch-white)"></span>
      <span class="swatch" style="background:var(--swatch-red)"></span>
      <span class="swatch" style="background:var(--swatch-graphite)"></span>
    </div>
  </article>
  <div class="abs btn" style="left:517px;top:605px;width:133px;height:53px">Pre-order</div>
  <p class="abs deposit-note">Pay the deposit today · balance due on shipping · mix colours in one order</p>
</section>

<!-- Video -->
<section class="abs" style="left:0;top:2008px;width:1200px;height:454px">
  <div class="photo" role="img" aria-label="Electric bikes parked at a charging station at sunset" style="left:0;top:0;width:1196px;height:454px;background:linear-gradient(160deg,#3d5366 0%,#c98a3a 35%,#e8b45a 55%,#6e4a26 80%,#2a2620 100%)"></div>
  <svg class="abs" style="left:514px;top:123px" width="160" height="160" viewBox="0 0 160 160">
    <circle cx="80" cy="80" r="78" fill="none" stroke="#fff" stroke-width="1.5" opacity=".85"/>
    <path d="M74 60l14 9-14 9z" fill="none" stroke="#fff" stroke-width="1.3"/>
  </svg>
  <div class="abs" style="left:514px;top:216px;width:160px;text-align:center;font-size:13px;font-weight:700;color:var(--white)">Product Video</div>
  <div class="abs serif" style="left:0;top:310px;width:1196px;text-align:center;font-size:44px;color:var(--white);letter-spacing:1px">Product Video</div>
</section>

<!-- Moments -->
<section class="abs" style="left:0;top:2462px;width:1200px;height:506px;background:var(--light-bg)">
  <div class="abs eyebrow" style="left:104px;top:108px">About our e-bikes</div>
  <h2 class="abs heading" style="left:104px;top:134px;font-size:46px;width:420px">Your Moments, Our Bikes</h2>
  <div class="abs rule" style="left:104px;top:266px"></div>
  <p class="abs copy" style="left:104px;top:292px;width:320px">Lorem ipsum dolor sit amet, consectetur adipiscing elit, sed do eiusmod tempor incididunt ut labore et dolor e magna aliqua. e magna aliqua. e magna</p>
  <div class="abs btn" style="left:102px;top:375px;width:133px;height:53px">Learn more</div>

  <div class="abs feature" style="left:579px;top:106px">
    <svg width="44" height="40" viewBox="0 0 44 40"><path d="M6 34a18 18 0 1 1 32 0" fill="none" stroke="#e8141b" stroke-width="2"/><path d="M22 20l-6-9" stroke="#e8141b" stroke-width="2"/><circle cx="22" cy="20" r="3" fill="none" stroke="#e8141b" stroke-width="2"/></svg>
    <div class="label">Quality<br>Craftsmanship</div><div class="num">1</div>
  </div>
  <div class="abs feature" style="left:842px;top:106px">
    <svg width="44" height="44" viewBox="0 0 44 44"><circle cx="22" cy="22" r="14" fill="none" stroke="#e8141b" stroke-width="2"/><circle cx="22" cy="22" r="6" fill="none" stroke="#e8141b" stroke-width="2"/><path d="M22 2v40M2 22h40" stroke="#e8141b" stroke-width="1.5"/></svg>
    <div class="label">Heritage and<br>History</div><div class="num">2</div>
  </div>
  <div class="abs feature" style="left:579px;top:270px">
    <svg width="40" height="40" viewBox="0 0 40 40"><circle cx="18" cy="9" r="5" fill="none" stroke="#e8141b" stroke-width="2"/><path d="M14 15l-6 14h14l6 6M4 36h32" fill="none" stroke="#e8141b" stroke-width="2"/></svg>
    <div class="label">Exclusive<br>Collections</div><div class="num">3</div>
  </div>
  <div class="abs feature" style="left:842px;top:270px">
    <svg width="40" height="40" viewBox="0 0 40 40"><path d="M20 4l13 9-5 16H12L7 13z" fill="none" stroke="#e8141b" stroke-width="2"/><circle cx="20" cy="4" r="2.5" fill="#e8141b"/><circle cx="33" cy="13" r="2.5" fill="#e8141b"/><circle cx="7" cy="13" r="2.5" fill="#e8141b"/></svg>
    <div class="label">Design<br>Excellence</div><div class="num">4</div>
  </div>
</section>

<!-- Precision -->
<section class="abs" style="left:0;top:2968px;width:1200px;height:492px">
  <div class="photo" role="img" aria-label="Row of green shared electric bikes at a docking station" style="left:0;top:0;width:1200px;height:492px;background:linear-gradient(110deg,#262a24 0%,#323a2c 45%,#2f5a2c 70%,#3f7a38 85%,#2a3a26 100%)"></div>
  <div class="abs" style="left:0;top:0;width:1200px;height:492px;background:rgba(20,20,20,.35)"></div>
  <h2 class="abs heading" style="left:153px;top:106px;font-size:56px;color:var(--white);width:640px;line-height:1.15">Precision and Passion in Every E-Bike</h2>
  <p class="abs copy" style="left:153px;top:278px;width:330px;color:#e6e6e6">Lorem ipsum dolor sit amet, consectetur adipiscing elit, sed do eiusmod tempor incididunt ut labore et dolor</p>
  <div class="abs btn" style="left:153px;top:341px;width:166px;height:49px">Go to product page</div>
</section>
<div class="abs" style="left:379px;top:3369px;width:661px;height:269px;background:var(--white)">
  <p class="abs serif" style="left:76px;top:60px;width:410px;font-size:15px;line-height:1.7;color:var(--text)">Lorem ipsum dolor sit amet, consectetur ad ipiscing elit, sed do eiusmod tempor incididunt ut labore et dolore magna aliqua. Ut enim ad minim veniam, quis nostrud exercitation ullamco laboris nisi ut aliquip ex ea commodo consequat. Duis aute irure dolor in reprehenderit</p>
  <svg class="abs" style="left:514px;top:100px" width="100" height="64" viewBox="0 0 100 64"><path d="M18 0a16 16 0 0 1 16 16c0 20-12 38-30 46l-3-5c10-6 16-14 16-24A16 16 0 0 1 18 0z" fill="#e8141b"/><path d="M70 0a16 16 0 0 1 16 16c0 20-12 38-30 46l-3-5c10-6 16-14 16-24A16 16 0 0 1 70 0z" fill="#e8141b"/></svg>
</div>

<!-- Contact -->
<section class="abs" style="left:0;top:3638px;width:1200px;height:663px">
  <div class="photo" role="img" aria-label="Mechanic in an orange sweater working on a bicycle wheel" style="left:151px;top:86px;width:359px;height:422px;background:linear-gradient(140deg,#e7d8c4 0%,#c88a4a 45%,#9a5a24 70%,#3a3430 100%)"></div>
  <div class="abs" style="left:239px;top:404px;width:271px;height:104px;background:var(--dark)">
    <svg class="abs" style="left:34px;top:36px" width="40" height="34" viewBox="0 0 40 34"><rect x="3" y="8" width="34" height="24" fill="none" stroke="#fff" stroke-width="1.4"/><path d="M3 8l17 13 17-13M8 8V2h24v6" fill="none" stroke="#fff" stroke-width="1.4"/></svg>
    <div class="abs" style="left:88px;top:40px;font-size:7px;letter-spacing:.4px;color:#aaa">NEED TO CONTACT US?</div>
    <div class="abs serif" style="left:88px;top:54px;font-size:18px;color:var(--white)">Email Us</div>
  </div>
  <div class="abs eyebrow" style="left:608px;top:59px">Contact with us</div>
  <h2 class="abs heading" style="left:608px;top:86px;font-size:46px">Any Questions?<br>Let’s Talk!</h2>
  <div class="abs rule" style="left:608px;top:213px"></div>
  <div class="abs field" style="left:606px;top:263px;width:214px;height:51px">My name is</div>
  <div class="abs field" style="left:825px;top:263px;width:215px;height:51px">My email</div>
  <div class="abs field" style="left:606px;top:317px;width:434px;height:51px">I am interested in</div>
  <div class="abs field" style="left:606px;top:374px;width:434px;height:134px">My message is</div>
  <div class="abs btn" style="left:896px;top:527px;width:144px;height:51px">Send a message</div>
</section>

<!-- Footer -->
<footer class="abs footer">
  <div class="abs foot-label" style="left:104px;top:106px">Visit office:</div>
  <div class="abs foot-value" style="left:104px;top:124px">48 Linden Ave. Riverside, 204</div>
  <div class="abs" style="left:104px;top:148px;width:34px;height:2px;background:var(--red)"></div>
  <div class="abs foot-label" style="left:104px;top:180px">Write email:</div>
  <div class="abs foot-value" style="left:104px;top:198px">hello@voltride-mail.com</div>
  <div class="abs" style="left:104px;top:222px;width:34px;height:2px;background:var(--red)"></div>
  <div class="abs foot-label" style="left:104px;top:255px">Make a call:</div>
  <div class="abs foot-value" style="left:104px;top:273px">0 (800)-555-72-30</div>

  <div class="abs" style="left:386px;top:118px;width:400px;text-align:center;font-size:76px;color:var(--white);line-height:1">VoltRide</div>
  <div class="abs serif" style="left:386px;top:252px;width:400px;text-align:center;font-size:13px;color:#bdbdc4;letter-spacing:1px">VOLTRIDE</div>
  <div class="abs serif" style="left:386px;top:272px;width:400px;text-align:center;font-size:11px;color:#9a9aa2">Clean. Quiet. Electric.</div>

  <div class="abs foot-label" style="left:869px;top:128px">Subscribe to our news</div>
  <div class="abs serif" style="left:869px;top:150px;width:240px;font-size:16px;line-height:1.3;color:var(--white)">Always Get Our Latest News &amp; Events Newsletter!</div>
  <div class="abs" style="left:869px;top:226px;width:178px;height:37px;background:#3a3a44;font-size:11px;color:#9a9aa2;padding:11px 18px">your email</div>
  <div class="abs" style="left:1053px;top:226px;width:47px;height:37px;background:var(--red);display:flex;align-items:center;justify-content:center">
    <svg width="10" height="14" viewBox="0 0 10 14"><path d="M2 1l6 6-6 6" fill="none" stroke="#fff" stroke-width="2.2"/></svg>
  </div>
</footer>

</body>
</html>
```